Brinewardsea.com Website design needed!!

We are looking for a website layout to match the attached logo. We specialize in Dive Charters and currently are located in the Virgin Islands off of St. Thomas. Please create a design that is compatible with Bootstrap and have the grid in mind. WE are looking for creative and extremely professional layout design.

Target Market(s)

Scuba Diving, Divers looking for a diving charter in the Virgin Islands.

Number of Pages Required

3 page

Font styles to use
Serif

Requirements
Must have
• Must be Bootstrap friendly.
• Must work with the logo we provided. Colors etc.

```html
<!DOCTYPE html>
<html lang="en">
<head>
<meta charset="utf-8">
<title>Brinewardsea – Dive Charters</title>
<link href="https://fonts.googleapis.com/css2?family=Raleway:wght@400;500;600&family=Open+Sans:wght@400;600&display=swap" rel="stylesheet">
<style>
:root{
  --navy:#0b1947;
  --navy-deep:#08133a;
  --ocean:#1466d6;
  --ocean-light:#2a8ff0;
  --sky:#2d9ad8;
  --accent:#1e8fd8;
  --red:#ee1c25;
  --white:#ffffff;
  --text:#222222;
  --muted:#666666;
  --rule:#cfcfcf;
  --footer:#0a8fdc;
}
*{margin:0;padding:0;box-sizing:border-box}
html,body{width:985px;height:1200px;overflow:hidden}
body{position:relative;font-family:"Open Sans",sans-serif;background:var(--white);color:var(--text)}
.abs{position:absolute}

.site-header{left:0;top:0;width:985px;height:108px;background:linear-gradient(180deg,var(--navy-deep),var(--navy))}
.brand{left:42px;top:38px;display:flex;align-items:center;gap:8px;font-family:"Raleway",sans-serif;font-weight:600;font-size:20px;color:var(--white)}
.brand-dot{width:14px;height:14px;border-radius:50%;background:var(--red)}
.main-nav{left:296px;top:40px;height:30px;display:flex;align-items:flex-end;font-family:"Raleway",sans-serif;font-size:12px;color:var(--white)}
.main-nav a{color:var(--white);text-decoration:none;padding:0 0 6px}
.nav-active{width:107px;height:30px;background:var(--red);border-radius:54px 54px 0 0 / 30px 30px 0 0;text-align:center;padding-top:13px!important}
.nav-about{margin-left:20px}
.nav-contact{margin-left:44px}
.nav-learn{margin-left:44px}
.nav-schedule{margin-left:44px}
.call{right:80px;top:38px;text-align:right;font-family:"Raleway",sans-serif}
.call-label{color:var(--accent);font-size:11px;font-weight:600;letter-spacing:.5px}
.call-number{color:var(--white);font-size:15px;font-weight:500;margin-top:2px}
.call-icon{left:910px;top:38px;width:33px;height:33px;border:1px solid var(--accent);border-radius:50%;display:flex;align-items:center;justify-content:center}

.hero{left:0;top:108px;width:985px;height:458px;background:
  radial-gradient(ellipse at 40% 30%,#2a7df0 0%,transparent 60%),
  linear-gradient(180deg,#1a5fd8 0%,#1552c0 55%,#2b6ab8 75%,#3a4f80 100%)}
.charter-form{left:632px;top:129px;width:300px;height:359px;background:rgba(14,44,140,.88);border:1px solid #6fa7e8}
.charter-form-head{height:64px;background:var(--sky);color:var(--white);font-family:"Raleway",sans-serif;font-size:18px;font-weight:500;text-align:center;line-height:22px;padding-top:11px}
.charter-form-intro{color:var(--white);font-size:9.5px;font-weight:600;text-align:center;line-height:13px;margin-top:17px}
.field{position:absolute;left:25px;width:252px;height:39px;border:1px solid var(--white);color:var(--white);font-size:11.5px;padding:15px 0 0 8px;text-transform:uppercase}
.field-dates{top:127px;height:40px}
.field-name{top:175px}
.field-email{top:224px}
.select-caret{position:absolute;right:7px;top:10px;width:18px;height:18px;background:#d8d8d8;border-radius:2px}
.find-btn{position:absolute;left:25px;top:289px;width:252px;height:40px;background:var(--red);color:var(--white);font-family:"Raleway",sans-serif;font-size:17px;text-align:center;line-height:40px;border-radius:2px}

.section-title{font-family:"Raleway",sans-serif;font-weight:500;text-align:center;white-space:nowrap}
.section-title span{color:var(--accent)}
.rule{height:1px;background:var(--rule)}
.welcome-title{left:0;width:985px;top:607px;font-size:24px;color:var(--text)}
.welcome-text{left:120px;width:745px;top:656px;font-size:10px;line-height:19px;color:var(--muted);text-align:center}
.read-more{left:447px;top:718px;width:101px;height:29px;background:var(--red);color:var(--white);font-size:9.5px;font-weight:600;text-align:center;line-height:29px}

.news{left:0;top:793px;width:985px;height:343px;background:
  radial-gradient(ellipse at 30% 80%,#3a4a5a 0%,transparent 55%),
  linear-gradient(180deg,#10284a 0%,#1c3550 60%,#2a3a4a 100%)}
.news-title{left:0;width:985px;top:834px;font-size:27px;color:var(--white)}
.news-thumb{left:206px;top:922px;width:153px;height:136px;border:1px solid var(--white);background:linear-gradient(160deg,#1b7aa0,#0d4c6a)}
.news-headline{left:407px;top:929px;font-family:"Raleway",sans-serif;font-size:19px;color:var(--red)}
.news-body{left:408px;top:966px;width:410px;font-size:10px;line-height:18.6px;color:var(--white)}
.more-dot{display:inline-block;width:10px;height:10px;border-radius:50%;background:var(--red);vertical-align:middle;margin-left:10px}

.site-footer{left:0;top:1136px;width:985px;height:64px;background:var(--footer)}
.copyright{left:42px;top:22px;font-size:10px;color:var(--white)}
.social{right:42px;top:29px;display:flex;gap:18px}
.social i{display:block;width:10px;height:10px;border-radius:50%;background:#cfe6f6}
</style>
</head>
<body>

<header class="site-header abs">
  <div class="brand abs"><i class="brand-dot"></i>Brinewardsea</div>
  <nav class="main-nav abs">
    <a class="nav-active" href="#">Brinewardsea</a>
    <a class="nav-about" href="#">About Us</a>
    <a class="nav-contact" href="#">Contact</a>
    <a class="nav-learn" href="#">Learn More</a>
    <a class="nav-schedule" href="#">Schedule</a>
  </nav>
  <div class="call abs">
    <div class="call-label">CALL US</div>
    <div class="call-number">(555)-013-2870</div>
  </div>
  <div class="call-icon abs">
    <svg width="16" height="16" viewBox="0 0 24 24" fill="none" stroke="#ffffff" stroke-width="2" stroke-linecap="round" stroke-linejoin="round"><path d="M5 3h4l2 5-2.5 1.5a11 11 0 0 0 6 6L16 13l5 2v4a2 2 0 0 1-2 2A16 16 0 0 1 3 5a2 2 0 0 1 2-2z"/></svg>
  </div>
</header>

<section class="hero abs" role="img" aria-label="Underwater photo of a scuba diver swimming above a coral reef"></section>

<form class="charter-form abs">
  <div class="charter-form-head">SEARCH FOR YOUR DREAM<br>CHARTER TODAY!</div>
  <p class="charter-form-intro">Lorem ipsum dolor sit amet, Consectetur<br>Adipiscing elit.</p>
  <div class="field field-dates">I have approximate dates
    <span class="select-caret"><svg width="18" height="18" viewBox="0 0 18 18"><path d="M6 8l3 3 3-3" stroke="#333" stroke-width="1.5" fill="none"/></svg></span>
  </div>
  <div class="field field-name">Name</div>
  <div class="field field-email">Email ID</div>
  <div class="find-btn">FIND CHARTERS</div>
</form>

<div class="rule abs" style="left:40px;top:622px;width:188px"></div>
<div class="rule abs" style="left:758px;top:622px;width:189px"></div>
<h1 class="section-title welcome-title abs">Welcome to <span>Brinewardsea Charters and Scuba</span></h1>
<p class="welcome-text abs">EHRs are supposed to enhance the practice of medicine, not slow it down. That’s why OP is built to move as quickly as you do. Our user interface is designed to follow your workflow – anticipating your needs and eliminating unnecessary</p>
<div class="read-more abs">READ MORE</div>

<section class="news abs" role="img" aria-label="Dark underwater coral reef background"></section>
<div class="rule abs" style="left:38px;top:853px;width:361px;background:#9aa8b8"></div>
<div class="rule abs" style="left:585px;top:853px;width:360px;background:#9aa8b8"></div>
<h2 class="section-title news-title abs">Latest <span>News</span></h2>
<svg class="abs" style="left:40px;top:948px" width="26" height="22" viewBox="0 0 26 22"><path d="M26 0L0 11l26 11-7-11z" fill="#d8d8d8"/></svg>
<svg class="abs" style="left:919px;top:948px" width="26" height="22" viewBox="0 0 26 22"><path d="M0 0l26 11L0 22l7-11z" fill="#d8d8d8"/></svg>
<div class="news-thumb abs" role="img" aria-label="Photo of a diver in mask and regulator underwater"></div>
<h3 class="news-headline abs">Caribbean Luxury Yacht Charter</h3>
<p class="news-body abs">A Caribbean luxury yacht charter is the most exclusive and most personalized way to explore the Caribbean. Whether you want to lounge in a top-deck hot tub, taste fine wines from an onboard cellar, or enjoy gourmet beach barbecues prepared by an award-winning chef, our team of dedicated professionals can help you book the Caribbean...<i class="more-dot"></i></p>

<footer class="site-footer abs">
  <p class="copyright abs">All Rights Reserved. Copyrights @company Name. 2016</p>
  <div class="social abs"><i></i><i></i><i></i><i></i><i></i></div>
</footer>

</body>
</html>
```